TV Media buying firm needs Lead Gen page layout

We need a landing page using our current website look and feel to capture leads from our Pixelnest ads. A quick form to capture Name, phone number, email, and a short message.
The call to action button should state "Get a free direct response campaign audit now!"
Updates

please visit www.brantwellmedia.com for the look and feel of the landing page.

I also uploaded a screenshot of what kind of landing page we are looking for.
the image has been reduced to 50% for the overall view.
thanks!

Please use our website's look and feel as reference for colors, fonts,header and footers.

The video placement on the sample file can be an image or combination image & text.

Again, please reference www.brantwellmedia.com for the look and feel.

Target Market(s)

50+ Market, Cheif Marketing Officer, Summit 1000 Companies

Industry/Entity Type

Tv

```html
<!DOCTYPE html>
<html lang="en">
<head>
<meta charset="utf-8">
<title>Brantwell Media – Direct Response Media Buying</title>
<link href="https://fonts.googleapis.com/css2?family=Montserrat:wght@400;600;700;800&family=Open+Sans:wght@400;600;700&display=swap" rel="stylesheet">
<style>
:root{
  --red:#c8102e;
  --ink:#1d1d1d;
  --text:#555;
  --header-bg:#f2f3f0;
  --nav-top:#3a3a3a;
  --nav-bottom:#0c0c0c;
  --panel:#f6f6f6;
  --green:#3d9a2c;
  --green-dark:#2c7a1e;
  --yellow:#f7c325;
  --section-alt:#f5f5f5;
  --footer-bg:#1f1f1f;
  --footer-text:#c9c9c9;
  --social:#3b4f7a;
}
*{box-sizing:border-box;margin:0;padding:0}
html,body{width:1200px;height:2268px;overflow:hidden}
body{font-family:"Open Sans",Arial,sans-serif;color:var(--text);background:#fff;position:relative}
.wrap{width:918px;margin:0 auto;position:relative}

/* header */
.site-header{height:166px;background:var(--header-bg);position:relative;border-bottom:1px solid #ddd}
.meta-line{position:absolute;left:141px;top:8px;font-size:11px;color:#555}
.social{position:absolute;left:880px;top:6px;display:flex;gap:14px}
.social span{width:36px;height:36px;border-radius:50%;background:var(--social);display:block}
.brand{position:absolute;left:141px;top:70px}
.brand-name{font-family:"Montserrat",sans-serif;font-weight:700;font-size:38px;color:var(--ink);line-height:1;display:flex;align-items:center;gap:12px}
.brand-name i{width:14px;height:14px;background:var(--red);display:block}
.call{position:absolute;left:868px;top:68px;display:flex;align-items:center;gap:8px}
.call-label{font-size:11px;color:#444;line-height:1}
.call-number{font-family:"Montserrat",sans-serif;font-size:23px;font-weight:600;color:var(--red);line-height:1.1}
.signup{position:absolute;left:620px;top:112px;width:438px;height:54px;background:#fff;border-radius:14px 14px 0 0;box-shadow:0 -2px 4px rgba(0,0,0,.08);display:flex;align-items:center;padding:0 14px 0 10px;gap:8px}
.signup-icon{width:34px;height:34px;border-radius:50%;background:#e07a1c;flex:none}
.signup-input{width:226px;height:30px;border:1px solid #bbb;border-radius:15px;font-size:13px;color:#666;padding:5px 14px}
.signup-btn{height:30px;padding:0 18px;border-radius:15px;background:var(--yellow);border:1px solid #d39a0c;font-family:"Montserrat",sans-serif;font-weight:700;font-size:14px;color:#222;display:flex;align-items:center}

/* nav */
.main-nav{height:50px;background:linear-gradient(var(--nav-top),var(--nav-bottom));border-bottom:3px solid #6a6a6a}
.main-nav ul{list-style:none;display:flex;height:47px;margin-left:135px}
.main-nav li{font-family:"Montserrat",sans-serif;color:#fff;font-size:15px;letter-spacing:.3px;padding:0 13px;display:flex;align-items:center;border-right:1px solid #555}
.main-nav li:last-child{border-right:none}

/* hero */
.hero{height:468px;background:linear-gradient(#dcdcdc,#ececec 40%,#e8e8e8);position:relative}
.video-frame{position:absolute;left:144px;top:37px;width:574px;height:393px;background:#fff;border:1px solid #ccc;border-radius:4px;box-shadow:0 2px 6px rgba(0,0,0,.18);padding:14px}
.video-screen{height:331px;background:linear-gradient(160deg,#f1f2f8,#b7bccd)}
.video-controls{height:32px;background:#1a1a1a;display:flex;align-items:center;padding:0 10px;gap:12px}
.video-controls .track{flex:1;height:5px;background:#666;border-radius:3px;position:relative}
.video-controls .track b{position:absolute;left:0;top:0;height:5px;width:40%;background:#bbb;border-radius:3px}
.video-controls .time{font-size:10px;color:#ccc}
.video-controls .vol{width:60px;height:5px;background:#8aa4cc;border-radius:3px}
.quick-form{position:absolute;left:748px;top:37px;width:310px;height:393px;background:var(--panel);border:1px solid #ccc;border-radius:4px;box-shadow:0 2px 6px rgba(0,0,0,.15);padding:6px}
.quick-form h2{height:44px;background:linear-gradient(#3d3d3d,#111);color:#fff;font-family:"Montserrat",sans-serif;font-weight:600;font-size:25px;text-align:center;line-height:44px;margin-bottom:12px}
.field{margin:0 12px 10px;height:40px;border:2px solid #cfcfcf;border-radius:5px;background:#fff;font-size:13px;color:#777;padding:9px 12px}
.field.msg{height:80px}
.cta{margin:6px 12px 0;height:64px;border-radius:5px;background:linear-gradient(var(--green),var(--green-dark));color:#fff;font-family:"Montserrat",sans-serif;font-weight:700;font-size:14px;text-align:center;display:flex;align-items:center;justify-content:center;line-height:1.6;text-transform:uppercase;letter-spacing:.3px}

/* partner strip */
.partners{height:125px;background:#fff;display:flex;align-items:center;justify-content:space-between;padding:0 140px}
.partner{font-family:"Montserrat",sans-serif;font-weight:700;font-size:21px;display:flex;align-items:center;gap:7px}
.partner i{width:14px;height:14px;border-radius:50%;background:currentColor;display:block}

/* what we do */
.services{height:504px;background:var(--section-alt);border-top:1px solid #e2e2e2;padding-top:36px}
.section-title{font-family:"Montserrat",sans-serif;font-weight:600;font-size:24px;color:var(--ink);text-transform:uppercase;margin-bottom:18px}
.ticks{list-style:none}
.ticks li{position:relative;padding-left:28px;font-size:14px;line-height:1.65;margin-bottom:15px;color:#5a5a5a}
.ticks svg{position:absolute;left:0;top:5px}

/* columns */
.columns{height:435px;background:#fff;padding-top:30px}
.columns .wrap{display:flex;gap:28px}
.col{width:290px}
.col h3{font-family:"Montserrat",sans-serif;font-weight:600;font-size:26px;color:var(--ink);text-transform:uppercase;margin-bottom:22px}
.col h3 span{color:var(--red)}
.entry{display:flex;gap:14px;height:113px}
.thumb{width:64px;height:76px;flex:none;background:linear-gradient(#d9dce3,#8b93a6);border:2px solid #ddd}
.entry p{font-size:13px;line-height:1.6;color:#666}
.entry .by,.entry a{color:var(--red);text-decoration:none}
.article{height:113px}
.article h4{font-weight:700;font-size:14px;color:#222;margin-bottom:6px}
.article p{font-size:13px;line-height:1.6;color:#666}
.article a{color:var(--red)}

/* clients */
.clients{height:195px;background:var(--section-alt);padding-top:12px}
.clients h2{font-family:"Montserrat",sans-serif;font-weight:400;font-size:25px;color:var(--ink);text-align:center;letter-spacing:.5px;margin-bottom:12px}
.client-row{display:flex;justify-content:center}
.client{width:246px;height:115px;display:flex;align-items:center;justify-content:center;background:linear-gradient(90deg,#f7f7f7,#fff 50%,#f1f1f1);font-family:"Montserrat",sans-serif;font-weight:700;font-size:21px;gap:8px}
.client i{width:14px;height:14px;display:block;background:currentColor}

/* footer */
.site-footer{height:212px;background:var(--footer-bg);color:var(--footer-text);text-align:center;font-size:12px;padding-top:32px}
.site-footer .links{width:880px;margin:0 auto;line-height:1.95}
.site-footer .sub{margin-top:20px}
.site-footer .tm{margin-top:22px}
.base{height:113px;background:#fff;text-align:center;padding-top:28px}
.base .brand-name{font-size:26px;justify-content:center}
.base .brand-name i{width:10px;height:10px}
.base small{display:block;font-size:12px;color:#333;margin-top:14px}
</style>
</head>
<body>

<header class="site-header">
  <p class="meta-line">DRTV, Media Buying, Direct Response Television, DRTV Advertising, World Class Media Buying Agency - Brantwell Media</p>
  <div class="social" aria-label="Social links: Pixelnest, Chirpline, Plusring, Linkfolio"><span></span><span></span><span></span><span></span></div>
  <div class="brand">
    <div class="brand-name"><i></i>Brantwell Media</div>
  </div>
  <div class="call">
    <svg width="30" height="30" viewBox="0 0 24 24" fill="none" stroke="#222" stroke-width="2"><path d="M4 14v-2a8 8 0 0 1 16 0v2"/><rect x="3" y="13" width="4" height="6" rx="1" fill="#222"/><rect x="17" y="13" width="4" height="6" rx="1" fill="#222"/></svg>
    <div><div class="call-label">Call Now</div><div class="call-number">555-014-2290</div></div>
  </div>
  <div class="signup">
    <span class="signup-icon"></span>
    <div class="signup-input">your@email.com</div>
    <div class="signup-btn">Sign Up Now</div>
  </div>
</header>

<nav class="main-nav">
  <ul>
    <li>WHAT WE DO</li><li>MEDIA SERVICES</li><li>TV RESOURCES</li><li>CLIENT PORTFOLIO</li><li>BLOG</li><li>ABOUT US</li><li>CONTACT</li>
  </ul>
</nav>

<section class="hero">
  <div class="video-frame">
    <div class="video-screen" role="img" aria-label="Video still: What's the difference between Image TV ads and DRTV?"></div>
    <div class="video-controls">
      <svg width="12" height="14" viewBox="0 0 12 14"><path d="M0 0l12 7-12 7z" fill="#fff"/></svg>
      <div class="track"><b></b></div>
      <span class="time">2:13 / 5:00</span>
      <svg width="16" height="14" viewBox="0 0 16 14"><path d="M0 4h4l5-4v14l-5-4H0z" fill="#fff"/></svg>
      <div class="vol"></div>
      <svg width="14" height="14" viewBox="0 0 14 14" fill="none" stroke="#fff" stroke-width="2"><path d="M1 5V1h4M9 1h4v4M13 9v4H9M5 13H1V9"/></svg>
    </div>
  </div>
  <form class="quick-form">
    <h2>QUICK FORM</h2>
    <div class="field">Enter Your Name</div>
    <div class="field">Enter Your Email</div>
    <div class="field">Enter Your Phone Number</div>
    <div class="field msg">Message</div>
    <div class="cta">Get a free direct response<br>campaign audit now</div>
  </form>
</section>

<section class="partners">
  <span class="partner" style="color:#1e4e9c"><i></i>Orbitline</span>
  <span class="partner" style="color:#222">HealthPage</span>
  <span class="partner" style="color:#9a6a1a">Ironwood Tools</span>
  <span class="partner" style="color:#c8102e">TaxTally</span>
  <span class="partner" style="color:#1a8fc6">RateQuote</span>
  <span class="partner" style="color:#1f3a78"><i></i>WallHero</span>
</section>

<section class="services">
  <div class="wrap">
    <h2 class="section-title">Direct Response Marketing Agency: What We Do</h2>
    <ul class="ticks">
      <li><svg width="14" height="12" viewBox="0 0 14 12"><path d="M1 6l4 4 8-9" fill="none" stroke="#4aa335" stroke-width="2.5"/></svg>One direct response company in the television industry is leading the charge to provide clients with an integrated, multi-channel direct response media buying strategy. That company is Brantwell Media.</li>
      <li><svg width="14" height="12" viewBox="0 0 14 12"><path d="M1 6l4 4 8-9" fill="none" stroke="#4aa335" stroke-width="2.5"/></svg>We integrate all the key mediums that comprise an effective direct response media buy, including DRTV - direct response television, online, print and radio; to ensure the success of the client's direct response media campaign.</li>
      <li><svg width="14" height="12" viewBox="0 0 14 12"><path d="M1 6l4 4 8-9" fill="none" stroke="#4aa335" stroke-width="2.5"/></svg>As a direct response agency, our staff works closely with our clients, guiding them through all stages of the media buying process, from DRTV media testing and analysis, through roll-out.</li>
      <li><svg width="14" height="12" viewBox="0 0 14 12"><path d="M1 6l4 4 8-9" fill="none" stroke="#4aa335" stroke-width="2.5"/></svg>Our approach enables Brantwell to deliver direct response media buys that lead to direct results.</li>
      <li><svg width="14" height="12" viewBox="0 0 14 12"><path d="M1 6l4 4 8-9" fill="none" stroke="#4aa335" stroke-width="2.5"/></svg>We know the 'ins' and 'outs' of maximizing the impact of a television direct response advertising campaign.</li>
      <li><svg width="14" height="12" viewBox="0 0 14 12"><path d="M1 6l4 4 8-9" fill="none" stroke="#4aa335" stroke-width="2.5"/></svg>The caliber of our direct response media buying performance is why marketers depend on Brantwell Media's professionals, campaign after campaign.</li>
      <li><svg width="14" height="12" viewBox="0 0 14 12"><path d="M1 6l4 4 8-9" fill="none" stroke="#4aa335" stroke-width="2.5"/></svg>Service to our clients is our top priority.</li>
      <li><svg width="14" height="12" viewBox="0 0 14 12"><path d="M1 6l4 4 8-9" fill="none" stroke="#4aa335" stroke-width="2.5"/></svg>Clients receive drtv media buying results that are measurable, specific and immediate.</li>
    </ul>
  </div>
</section>

<section class="columns">
  <div class="wrap">
    <div class="col">
      <h3>Client's <span>Speak</span></h3>
      <div class="entry"><div class="thumb" role="img" aria-label="Client portrait photo"></div><p>"Brantwell Media's effective and efficient direct response media buying expertise...<br><span class="by">-Client Name</span></p></div>
      <div class="entry"><div class="thumb" role="img" aria-label="Client portrait photo"></div><p>"Brantwell Media's effective and efficient direct response media buying expertise...<br><span class="by">-Client Name</span></p></div>
      <div class="entry"><div class="thumb" role="img" aria-label="Client portrait photo"></div><p>"Brantwell Media's effective and efficient direct response media buying expertise...<br><span class="by">-Client Name</span></p></div>
    </div>
    <div class="col">
      <h3>DRTV <span>Articles</span></h3>
      <div class="article"><h4>What is Media Buying?</h4><p>Media buying is the process of buying advertising space or time in order to display company' advertising...<a>[Read More]</a></p></div>
      <div class="article"><h4>What is Media Buying?</h4><p>Media buying is the process of buying advertising space or time in order to display company' advertising...<a>[Read More]</a></p></div>
      <div class="article"><h4>What is Media Buying?</h4><p>Media buying is the process of buying advertising space or time in order to display company' advertising...<a>[Read More]</a></p></div>
    </div>
    <div class="col">
      <h3>Latest <span>News</span></h3>
      <div class="entry"><div class="thumb" role="img" aria-label="News photo of agency team"></div><p>The Austin-based media buying agency's longstanding foc research groundbreaking profiling ...<a>[Read More]</a></p></div>
      <div class="entry"><div class="thumb" role="img" aria-label="News photo of agency team"></div><p>The Austin-based media buying agency's longstanding foc research groundbreaking profiling ...<a>[Read More]</a></p></div>
      <div class="entry"><div class="thumb" role="img" aria-label="News photo of agency team"></div><p>The Austin-based media buying agency's longstanding foc research groundbreaking profiling ...<a>[Read More]</a></p></div>
    </div>
  </div>
</section>

<section class="clients">
  <h2>OUR CLIENTS</h2>
  <div class="client-row">
    <div class="client" style="color:#c8102e"><i></i>Meridian Electric</div>
    <div class="client" style="color:#c8102e">Kaito</div>
    <div class="client" style="color:#1b4f9a">Coolstream Air</div>
    <div class="client" style="color:#1b3f8a">Veltronic</div>
    <div class="client" style="color:#2a6fb0">Arcwave</div>
  </div>
</section>

<footer class="site-footer">
  <p class="links">Drtv home | about us | key management | services | direct response television | drtv infomercial | online direct response | radio direct response<br>print direct response | drtv lead generation | branded drtv | senior marketing specialist | media buying services | television media buying<br>media buyer planning | reporting &amp; analysis | case studies | resources | client portfolio | past articles | contact us | site map</p>
  <p class="sub">Brantwell Interactive | Multi-Platform Media Buying | Infomercial</p>
  <p class="tm">Multi-Platform Media Buying is a service of Brantwell, Brantwell Media and Brantwell Interactive.</p>
</footer>

<div class="base">
  <div class="brand-name"><i></i>Brantwell Media</div>
  <small>© 2014 Brantwell Media. All Rights Reserved.</small>
</div>

</body>
</html>
```